Advertisement flyer for fire sprinkler repair parts. The projected audience are contractors.

I need a flyer advertising specific parts that we are stocking at our company "Meridian Valvecraft Supply." I have attached a picture of our logo. I want the title to say "Fire Pump Repair Parts and Accessories." I want to specifically advertise the following parts: Repack Kits and Repair Parts, Jockey Pumps, Pump Controllers, Casing Relief Valves, Air Release Valves, Suction/Discharge Gauges, Pump Shaft Couplers & Shim Kits, Fire Pump Relief Valves, and QN Listed Pressure Reducing Valves. I have attached pictures of the manufacturers I want to advertise on this flyer. I have also attached pictures of some of the parts we are stocking that I would like to be included somewhere in the flyer. I would like all of the pictures to have a transparent background. Also I would like our phone number :(800)-431-2867, and our website www.tolvenspares.example included. I made my own design that I have Attached. You do not have to go based off this design, but I would like the basic content to be the same. We do have Same- Day shipping as well as Free Tech Support if you can include that anywhere.

```html
<!DOCTYPE html>
<html lang="en">
<head>
<meta charset="utf-8">
<title>Meridian Valvecraft Supply – Fire Pump Repair Parts Flyer</title>
<link rel="stylesheet" href="https://fonts.googleapis.com/css2?family=Arimo:wght@400;700&family=Source+Sans+3:wght@400&display=swap">
<style>
  :root {
    --page-bg: #e4e7e8;
    --brand-blue: #2f4aa0;
    --brand-blue-dark: #23397f;
    --title-red: #cc0f2e;
    --label-blue: #2b3f9a;
    --card-white: #ffffff;
    --placeholder-grey: #8d8d8d;
    --band-white: #ffffff;
    --ink: #2a2f3a;
  }
  * { box-sizing: border-box; margin: 0; padding: 0; }
  html, body { width: 1200px; height: 2250px; overflow: hidden; }
  body {
    background: var(--page-bg);
    font-family: "Arimo", Arial, sans-serif;
    position: relative;
  }
  .flyer {
    position: absolute;
    left: 40px; top: 402px;
    width: 1120px; height: 1445px;
    background: #fff;
    overflow: hidden;
    box-shadow: 0 14px 30px rgba(0,0,0,.35);
  }
  .hero-photo {
    position: absolute; left: 0; top: 0; width: 1120px; height: 575px;
    background:
      radial-gradient(ellipse at 45% 70%, #b3261f 0%, rgba(179,38,31,0) 45%),
      radial-gradient(ellipse at 80% 40%, #a9221c 0%, rgba(169,34,28,0) 40%),
      linear-gradient(180deg, #6e6a66 0%, #8d857c 40%, #5b4b43 100%);
  }
  .frame-shapes { position: absolute; left: 0; top: 0; }
  .brand {
    position: absolute; left: 40px; top: 40px;
    display: flex; align-items: center; gap: 20px;
  }
  .brand-mark { width: 72px; height: 72px; background: var(--title-red); }
  .brand-name {
    font-family: "Source Sans 3", Arial, sans-serif;
    font-weight: 400; color: var(--brand-blue);
    font-size: 40px; line-height: 1;
  }
  .brand-name span { display: block; font-size: 22px; margin-top: 4px; }
  .parts-backdrop {
    position: absolute; left: 0; top: 575px; width: 1120px; height: 655px;
    background:
      radial-gradient(ellipse at 30% 40%, rgba(255,255,255,.8) 0%, rgba(255,255,255,0) 35%),
      radial-gradient(ellipse at 75% 65%, rgba(255,255,255,.7) 0%, rgba(255,255,255,0) 35%),
      linear-gradient(180deg, #c9c7c2 0%, #b6b0a6 50%, #cfccc6 100%);
  }
  .headline {
    position: absolute; left: 0; top: 582px; width: 1120px;
    text-align: center; font-weight: 700; font-size: 50px;
    color: var(--title-red);
    text-shadow: 2px 2px 0 #fff, -1px -1px 0 #fff, 1px -1px 0 #fff, -1px 1px 0 #fff;
  }
  .part {
    position: absolute; width: 300px; text-align: center;
  }
  .part-card {
    margin: 0 auto; width: 206px; height: 126px;
    background: var(--card-white);
    transform: skewX(-10deg);
    box-shadow: 0 4px 10px rgba(0,0,0,.2);
    display: flex; align-items: center; justify-content: center;
  }
  .part-card.is-bare { background: transparent; box-shadow: none; }
  .placeholder {
    transform: skewX(10deg);
    color: var(--placeholder-grey); font-size: 28px; line-height: 1.15;
  }
  .product-shot { transform: skewX(10deg); }
  .part-name {
    margin-top: 14px; font-weight: 700; font-size: 20px; color: var(--label-blue);
    white-space: nowrap;
  }
  .maker-band {
    position: absolute; left: 0; top: 1230px; width: 1120px; height: 100px;
    background: var(--band-white);
    display: flex; align-items: center; justify-content: space-around;
    padding: 0 20px;
  }
  .maker { font-weight: 700; font-size: 20px; color: var(--brand-blue-dark); }
  .contact-bar { position: absolute; left: 0; top: 1330px; }
  .contact-text {
    position: absolute; left: 0; top: 1342px; width: 1120px;
    text-align: center; color: #fff;
  }
  .contact-phone { font-weight: 700; font-size: 50px; line-height: 1.1; }
  .contact-web { font-size: 30px; margin-top: 6px; }
</style>
</head>
<body>
  <main class="flyer">
    <div class="hero-photo" role="img" aria-label="Photo of a fire pump room with red piping and valves"></div>

    <svg class="frame-shapes" width="1120" height="590" viewBox="0 0 1120 590" aria-hidden="true">
      <polygon points="0,0 655,0 575,155 0,155" fill="#ffffff"/>
      <polygon points="655,0 680,0 600,155 575,155" fill="var(--brand-blue)"/>
      <polygon points="0,535 420,535 455,568 1120,568 1120,590 0,590" fill="var(--brand-blue)"/>
    </svg>

    <div class="brand">
      <div class="brand-mark"></div>
      <div class="brand-name">Meridian Valvecraft<span>Supply</span></div>
    </div>

    <div class="parts-backdrop" role="img" aria-label="Soft background photo of splashing water"></div>

    <h1 class="headline">Fire Pump Repair Parts &amp; Accessories!</h1>

    <section class="parts-grid">
      <div class="part" style="left:83px;top:672px">
        <div class="part-card"><div class="placeholder">Product<br>Image<br>here</div></div>
        <p class="part-name">Fire Pump Repack Kits</p>
      </div>
      <div class="part" style="left:410px;top:672px">
        <div class="part-card is-bare"><div class="product-shot" role="img" aria-label="Jockey pump unit" style="width:190px;height:110px;background:linear-gradient(135deg,#c8201b,#8e1612);border-radius:10px"></div></div>
        <p class="part-name">Jockey Pumps</p>
      </div>
      <div class="part" style="left:739px;top:672px">
        <div class="part-card is-bare"><div class="product-shot" role="img" aria-label="Brass pump controller valve" style="width:80px;height:124px;background:linear-gradient(180deg,#9a8a58,#6e5a2a);border-radius:8px"></div></div>
        <p class="part-name">Pump Controllers</p>
      </div>

      <div class="part" style="left:83px;top:853px">
        <div class="part-card is-bare"><div class="product-shot" role="img" aria-label="Casing relief valve" style="width:60px;height:124px;background:linear-gradient(180deg,#d9d2c4,#3b6fb0);border-radius:6px"></div></div>
        <p class="part-name">Casing Relief Valves</p>
      </div>
      <div class="part" style="left:410px;top:853px">
        <div class="part-card"><div class="placeholder">Product<br>Image<br>here</div></div>
        <p class="part-name">Air Release Valves</p>
      </div>
      <div class="part" style="left:739px;top:853px">
        <div class="part-card"><div class="placeholder">Product<br>Image<br>here</div></div>
        <p class="part-name">Suction/Discharge Gauges</p>
      </div>

      <div class="part" style="left:83px;top:1033px">
        <div class="part-card" role="img" aria-label="Pump shaft couplers and shim kit parts" style="background:linear-gradient(135deg,#a8957c,#6f6658)"></div>
        <p class="part-name">Pump Shaft Couplers &amp; Shim Kits</p>
      </div>
      <div class="part" style="left:410px;top:1033px">
        <div class="part-card"><div class="placeholder">Product<br>Image<br>here</div></div>
        <p class="part-name">Fire Pump Relief Valves</p>
      </div>
      <div class="part" style="left:739px;top:1033px">
        <div class="part-card"><div class="placeholder">Product<br>Image<br>here</div></div>
        <p class="part-name">QN Listed Pressure Reducing Valves.</p>
      </div>
    </section>

    <div class="maker-band">
      <span class="maker">Borealis</span>
      <span class="maker">Kestrel Hollow</span>
      <span class="maker">Tundrix</span>
      <span class="maker">Voxa</span>
      <span class="maker">Calder</span>
      <span class="maker">Brightline</span>
      <span class="maker">Ostrava</span>
      <span class="maker">Veldon</span>
    </div>

    <svg class="contact-bar" width="1120" height="115" viewBox="0 0 1120 115" aria-hidden="true">
      <polygon points="44,0 1076,0 1120,46 1120,115 0,115 0,46" fill="var(--brand-blue)"/>
    </svg>
    <div class="contact-text">
      <p class="contact-phone">Call Us Today: (800) 431-2867</p>
      <p class="contact-web">visit us www.tolvenspares.example</p>
    </div>
  </main>
</body>
</html>
```